Quillnest - New Website Design

Create a professional Shopify website for the hottest trend; a box of school supplies subscription box business called Quillnest. Pagevane.com is an easy to use website builder.
Please see frindlepak.com; sweelohut.com; trimvalegroupe.com; and wagtrunk.com for the concept I am after. The business has not been launched yet, I am currently in the pre-launch stage using a specialized landing page website, and so the time scale for developing my professional looking Shopify website is up to 1-2 weeks.
The webpage should have a fun feel and should match the style of the company logo at sweelohut.com. The pages to include are 'Home', 'About us' and 'Get Started'
Thank you and good luck!
1 page

```html
<!DOCTYPE html>
<html lang="en">
<head>
<meta charset="utf-8">
<title>Quillnest — School Supplies Subscription Box</title>
<link rel="stylesheet" href="https://fonts.googleapis.com/css2?family=Roboto+Condensed:wght@400;700&family=Righteous&family=Damion&display=swap">
<style>
  :root {
    --pink: #f2126b;
    --teal: #2fd6c3;
    --blue: #0ea6e9;
    --ink: #111111;
    --text: #4a4a4a;
    --muted: #666666;
    --footer-bg: #2a2a2e;
    --footer-text: #d6d6d6;
    --white: #ffffff;
  }
  * { box-sizing: border-box; margin: 0; padding: 0; }
  html, body { width: 1200px; height: 2233px; overflow: hidden; }
  body {
    position: relative;
    background: var(--white);
    font-family: "Roboto Condensed", "Arial Narrow", sans-serif;
    color: var(--text);
  }

  /* Header */
  .site-header { position: absolute; left: 0; top: 0; width: 1200px; height: 68px; background: var(--white); }
  .brand { position: absolute; left: 112px; top: 16px; display: flex; align-items: center; gap: 10px;
    font-weight: 700; font-size: 28px; color: var(--teal); letter-spacing: 0.5px; }
  .brand-mark { width: 22px; height: 22px; background: var(--teal); border-radius: 4px; }
  .main-nav { position: absolute; top: 24px; left: 0; width: 1200px; font-size: 15px; }
  .main-nav a { position: absolute; text-decoration: none; color: var(--blue); white-space: nowrap; }
  .main-nav a.nav-cta { color: var(--pink); }

  /* Buttons */
  .btn { position: absolute; display: flex; align-items: center; justify-content: center;
    color: var(--white); font-weight: 700; font-size: 16px; text-decoration: none; border-radius: 2px; }
  .btn-pink { background: var(--pink); }
  .btn-blue { background: var(--blue); }
  .btn-teal { background: var(--teal); }

  /* Hero */
  .hero { position: absolute; left: 0; top: 68px; width: 1200px; height: 514px; overflow: hidden;
    background: repeating-linear-gradient(90deg, #e9f0f1 0 22px, #dfe8e9 22px 26px, #edf3f3 26px 48px); }
  .hero-title { position: absolute; left: 112px; top: 112px; font-family: "Righteous", sans-serif;
    font-size: 33px; line-height: 37px; color: var(--pink); letter-spacing: 0.5px; text-transform: uppercase; }
  .hero-title .accent { color: var(--teal); }
  .hero-lead { position: absolute; left: 112px; top: 200px; width: 400px; font-size: 15px; line-height: 22px; color: var(--ink); }
  .hero-visual { position: absolute; left: 476px; top: 126px; width: 656px; height: 357px; border-radius: 6px;
    background: radial-gradient(ellipse at 60% 60%, #c9a77a 0%, #d8c0a0 40%, rgba(230,238,239,0) 75%); }

  /* Section titles */
  .section-title { position: absolute; left: 0; width: 1200px; text-align: center;
    font-family: "Damion", cursive; font-weight: 400; font-size: 40px; color: var(--ink); line-height: 1; }

  /* Steps */
  .step { position: absolute; top: 700px; width: 290px; text-align: center; }
  .step-badge { display: block; margin: 0 auto; width: 72px; height: 72px; }
  .step-title { margin-top: 18px; font-size: 19px; font-weight: 700; color: var(--ink); }
  .step-text { margin-top: 14px; font-size: 15px; line-height: 22.5px; color: var(--muted); padding: 0 10px; }

  /* Inside the box */
  .inside { position: absolute; left: 0; top: 1051px; width: 1200px; height: 441px; overflow: hidden;
    background: linear-gradient(115deg, #dfe9ea 0%, #eef4f4 35%, #e7eff0 65%, #dde8e9 100%); }
  .inside-visual { position: absolute; left: 116px; top: 88px; width: 468px; height: 302px; border-radius: 6px;
    background: radial-gradient(ellipse at 55% 55%, #e7b37c 0%, #e9c39d 35%, rgba(233,240,241,0) 72%); }
  .inside-title { position: absolute; left: 620px; top: 84px; width: 460px; text-align: center;
    font-family: "Damion", cursive; font-weight: 400; font-size: 38px; color: var(--ink); }
  .inside-text { position: absolute; left: 660px; top: 143px; width: 385px; text-align: center;
    font-size: 15px; line-height: 22.3px; color: var(--muted); }

  /* Testimonials */
  .divider { position: absolute; left: 600px; top: 1620px; width: 1px; height: 241px; background: #e3e3e3; }
  .review { position: absolute; top: 1622px; width: 420px; text-align: center; }
  .avatar { margin: 0 auto; width: 104px; height: 104px; border-radius: 50%; border: 3px solid var(--blue);
    background: linear-gradient(160deg, #e3c7ad, #b98a6a); }
  .review-quote { margin-top: 26px; font-size: 15px; line-height: 22.5px; color: var(--muted); }
  .review-name { margin-top: 14px; font-size: 16px; font-weight: 700; color: var(--pink); }
  .review-role { font-size: 13px; color: var(--muted); }

  /* Footer */
  .site-footer { position: absolute; left: 0; top: 1989px; width: 1200px; height: 244px; background: var(--footer-bg); color: var(--footer-text); }
  .footer-brand { position: absolute; left: 112px; top: 50px; display: flex; align-items: center; gap: 10px;
    font-weight: 700; font-size: 26px; color: var(--teal); }
  .footer-brand .brand-mark { width: 20px; height: 20px; }
  .footer-col { position: absolute; top: 36px; }
  .footer-col h4 { font-size: 15px; font-weight: 700; color: var(--white); margin-bottom: 10px; }
  .footer-col a { display: block; font-size: 13px; line-height: 22.3px; color: var(--footer-text); text-decoration: none; }
  .social-list { display: flex; gap: 3px; margin-top: 4px; }
  .social-dot { width: 28px; height: 28px; border-radius: 50%; border: 1.5px solid #bdbdbd; }
  .newsletter-title { font-family: "Damion", cursive; font-size: 22px; color: var(--white); margin-bottom: 12px; }
  .newsletter-input { width: 225px; height: 36px; background: var(--white); border-radius: 2px; padding: 0 12px;
    display: flex; align-items: center; font-size: 14px; color: #9a9a9a; }
  .newsletter-btn { margin-top: 9px; width: 225px; height: 36px; background: var(--teal); border-radius: 2px;
    display: flex; align-items: center; justify-content: center; color: var(--white); font-weight: 700; font-size: 16px; }
  .footer-rule { position: absolute; left: 112px; top: 197px; width: 977px; height: 1px; background: #3c3c41; }
  .copyright { position: absolute; left: 112px; top: 213px; font-size: 13px; }
  .legal-links { position: absolute; right: 111px; top: 213px; font-size: 13px; display: flex; gap: 14px; }
  .legal-links a { color: var(--footer-text); text-decoration: none; }
</style>
</head>
<body>

<header class="site-header">
  <div class="brand"><span class="brand-mark"></span>Quillnest</div>
  <nav class="main-nav">
    <a href="#" style="left:862px">Home</a>
    <a href="#" style="left:932px">About Us</a>
    <a href="#" class="nav-cta" style="left:1021px">Get Started</a>
  </nav>
</header>

<section class="hero">
  <h1 class="hero-title">Lorem ipsum dolor sit amet<br>as well as <span class="accent">consectetur</span></h1>
  <p class="hero-lead">Nullam ac urna eu felis dapibus condimentum sit amet a augue. Sed non neque elit. Sed ut imperdiet nisi. Proin condimentum fermentum nunc.</p>
  <a class="btn btn-pink" href="#" style="left:112px; top:289px; width:141px; height:39px;">Get Started</a>
  <a class="btn btn-blue" href="#" style="left:262px; top:289px; width:140px; height:39px;">Give A Gift</a>
  <div class="hero-visual" role="img" aria-label="Cardboard box overflowing with school supplies beside a globe, pencil cup and toy school bus"></div>
</section>

<h2 class="section-title" style="top:630px;">How it Works</h2>

<div class="step" style="left:120px;">
  <svg class="step-badge" viewBox="0 0 72 72" aria-hidden="true">
    <path d="M36 2 C52 2 70 34 70 48 C70 62 56 70 36 70 C16 70 2 62 2 48 C2 34 20 2 36 2 Z" fill="var(--blue)"/>
    <text x="36" y="47" text-anchor="middle" font-family="Roboto Condensed, sans-serif" font-weight="700" font-style="italic" font-size="22" fill="#fff">01</text>
  </svg>
  <div class="step-title">Lorem ipsum dolor sit</div>
  <p class="step-text">Duis sed odio sit amet nibh vulputate cursus a sit amet mauris. Morbi accumsan ipsum Nam nec tellus a odio tincidunt auctor a ornare odio. neque elit.</p>
</div>
<div class="step" style="left:455px;">
  <svg class="step-badge" viewBox="0 0 72 72" aria-hidden="true">
    <path d="M36 2 C52 2 70 34 70 48 C70 62 56 70 36 70 C16 70 2 62 2 48 C2 34 20 2 36 2 Z" fill="var(--pink)"/>
    <text x="36" y="47" text-anchor="middle" font-family="Roboto Condensed, sans-serif" font-weight="700" font-style="italic" font-size="22" fill="#fff">02</text>
  </svg>
  <div class="step-title">Lorem ipsum dolor sit</div>
  <p class="step-text">Duis sed odio sit amet nibh vulputate cursus a sit amet mauris. Morbi accumsan ipsum Nam nec tellus a odio tincidunt auctor a ornare odio. neque elit.</p>
</div>
<div class="step" style="left:789px;">
  <svg class="step-badge" viewBox="0 0 72 72" aria-hidden="true">
    <path d="M36 2 C52 2 70 34 70 48 C70 62 56 70 36 70 C16 70 2 62 2 48 C2 34 20 2 36 2 Z" fill="var(--teal)"/>
    <text x="36" y="47" text-anchor="middle" font-family="Roboto Condensed, sans-serif" font-weight="700" font-style="italic" font-size="22" fill="#fff">03</text>
  </svg>
  <div class="step-title">Lorem ipsum dolor sit</div>
  <p class="step-text">Duis sed odio sit amet nibh vulputate cursus a sit amet mauris. Morbi accumsan ipsum Nam nec tellus a odio tincidunt auctor a ornare odio. neque elit.</p>
</div>

<a class="btn btn-pink" href="#" style="left:530px; top:960px; width:140px; height:39px;">Get Started</a>

<section class="inside">
  <div class="inside-visual" role="img" aria-label="Open cardboard box with notebooks, folders, coloured pencils and markers"></div>
  <h2 class="inside-title">What’s inside the Box</h2>
  <p class="inside-text">Class aptent taciti sociosqu ad litora torquent per conubia nostra, per inceptos himenaeos. Mauris in erat justo. Nullam ac urna eu felis dapibus condimentum sit amet a augue. Sed non neque elit. Sed ut imperdiet nisi. Proin condimentum fermentum nunc. Etiam pharetra, erat sed fermentum feugiat, velit mauris egestas quam, ut aliquam massa nisl quis neque. Suspendisse in orci enim.</p>
  <a class="btn btn-teal" href="#" style="left:780px; top:316px; width:140px; height:39px;">Explore More</a>
</section>

<h2 class="section-title" style="top:1540px;">Happy Customer</h2>

<div class="divider"></div>

<div class="review" style="left:138px;">
  <div class="avatar" role="img" aria-label="Customer portrait"></div>
  <p class="review-quote">“ Proin condimentum fermentum nunc. Etiam pharetra, erat sed fermentum feugiat, velit mauris egestas quam, ut aliquam massa nisl quis neque. Suspendisse in orci velit mauris egestas quam enim.”</p>
  <div class="review-name">Shopia</div>
  <div class="review-role">lorem ipsum dolor</div>
</div>
<div class="review" style="left:642px;">
  <div class="avatar" role="img" aria-label="Customer portrait"></div>
  <p class="review-quote">“ Proin condimentum fermentum nunc. Etiam pharetra, erat sed fermentum feugiat, velit mauris egestas quam, ut aliquam massa nisl quis neque. Suspendisse in orci velit mauris egestas quam enim.”</p>
  <div class="review-name">William doe</div>
  <div class="review-role">lorem ipsum dolor</div>
</div>

<a class="btn btn-blue" href="#" style="left:473px; top:1898px; width:254px; height:41px;">View More Customer Reviews</a>

<footer class="site-footer">
  <div class="footer-brand"><span class="brand-mark"></span>Quillnest</div>

  <div class="footer-col" style="left:317px;">
    <h4>Subscribe</h4>
    <a href="#">Get Started</a>
    <a href="#">Get a Quillnest</a>
    <a href="#">Give a Gift</a>
    <a href="#">Claim a Gift</a>
  </div>
  <div class="footer-col" style="left:505px;">
    <h4>Info</h4>
    <a href="#">About Quillnest</a>
    <a href="#">Our Story</a>
    <a href="#">Contact Us</a>
    <a href="#">FAQs</a>
  </div>
  <div class="footer-col" style="left:660px;">
    <h4>We’re Social</h4>
    <div class="social-list">
      <span class="social-dot"></span><span class="social-dot"></span><span class="social-dot"></span><span class="social-dot"></span><span class="social-dot"></span>
    </div>
  </div>
  <div class="footer-col" style="left:864px;">
    <div class="newsletter-title">Subcribe Newsletter</div>
    <div class="newsletter-input">Name</div>
    <div class="newsletter-btn">Subscribe</div>
  </div>

  <div class="footer-rule"></div>
  <div class="copyright">Copyright ©2017 Quillnest.</div>
  <div class="legal-links"><a href="#">Terms of Use</a><a href="#">Privacy</a><a href="#">Sitemap</a></div>
</footer>

</body>
</html>
```